Indian Lunch Delivery company needs a google ad banner for advertising its offering

We are a Kolkata, India based startup delivering lunch to office buildings in the city. We only serve set meals (vegetarian and non-vegetarian). Minimum order quantity is 5 boxes. The name of the brand is Verdopan (Thali=platter). Our USP-
We cook fresh
Trans-fat free
No emulsifiers, preservatives or artificial colorings used.
Importantly, we are a value for money brand. To be precise our meals costs just .99 c.
Target Market(s)
Young professionals
Industry/Entity Type
It Company
Font styles to use
Sans Serif
Requirements
Must have
- Home made food feel to it
Nice to have
- Lots of colours

```html
<!DOCTYPE html>
<html lang="en">
<head>
<meta charset="utf-8">
<title>Verdopan – Cooked Fresh Daily, Set Meals at $0.99</title>
<link rel="stylesheet" href="https://fonts.googleapis.com/css2?family=Parisienne&family=Roboto+Condensed:wght@400;700&family=Roboto:wght@700&display=swap">
<style>
  :root {
    --bg: #ffffff;
    --mint: #5fc9a1;
    --salmon: #ef7f6e;
    --white: #ffffff;
    --food-warm: #c9773e;
    --food-deep: #a9543a;
    --food-light: #eadfcf;
    --food-green: #7aa24a;
  }
  html, body {
    margin: 0;
    padding: 0;
    overflow: hidden;
    background: var(--bg);
  }
  .banner {
    position: relative;
    width: 1200px;
    height: 232px;
    overflow: hidden;
    background: var(--bg);
  }
  .meal-photo {
    position: absolute;
    left: 0;
    top: 0;
    width: 280px;
    height: 232px;
  }
  .brand {
    position: absolute;
    left: 316px;
    top: 50px;
    width: 220px;
    color: var(--mint);
    line-height: 1;
  }
  .brand-name {
    display: block;
    font-family: "Parisienne", cursive;
    font-size: 62px;
    line-height: 1;
  }
  .brand-service {
    display: block;
    font-family: "Roboto Condensed", sans-serif;
    font-weight: 700;
    font-size: 50px;
    letter-spacing: 1px;
    margin-top: -4px;
  }
  .headline-box {
    position: absolute;
    left: 571px;
    top: 28px;
    width: 432px;
    height: 175px;
    background: var(--salmon);
  }
  .headline-box::before,
  .headline-box::after {
    content: "";
    position: absolute;
    top: 0;
    bottom: 0;
    width: 2px;
    background: var(--white);
  }
  .headline-box::before { left: 9px; }
  .headline-box::after { right: 9px; }
  .headline {
    margin: 0;
    position: absolute;
    left: 0;
    right: 0;
    top: 32px;
    text-align: center;
    color: var(--white);
    font-family: "Roboto Condensed", sans-serif;
    font-weight: 400;
    font-size: 43px;
    line-height: 58px;
    letter-spacing: 0.3px;
  }
  .cta {
    position: absolute;
    left: 1029px;
    top: 99px;
    width: 144px;
    height: 51px;
    border-radius: 5px;
    background: var(--mint);
    color: var(--white);
    font-family: "Roboto", sans-serif;
    font-weight: 700;
    font-size: 14px;
    letter-spacing: 0.5px;
    display: flex;
    align-items: center;
    justify-content: center;
    text-decoration: none;
  }
</style>
</head>
<body>
  <div class="banner">
    <svg class="meal-photo" viewBox="0 0 280 232" role="img" aria-label="Photo of a home-style Indian thali: rice with peas, curry, naan, cucumber and lime">
      <defs>
        <radialGradient id="meal-tones" cx="40%" cy="55%" r="70%">
          <stop offset="0" stop-color="var(--food-warm)"/>
          <stop offset="0.45" stop-color="var(--food-deep)"/>
          <stop offset="0.75" stop-color="var(--food-light)"/>
          <stop offset="1" stop-color="var(--food-green)"/>
        </radialGradient>
      </defs>
      <circle cx="122" cy="116" r="154" fill="url(#meal-tones)"/>
    </svg>

    <div class="brand">
      <span class="brand-name">Verdopan</span>
      <span class="brand-service">DELIVERY</span>
    </div>

    <div class="headline-box">
      <h1 class="headline">COOKED FRESH DAILY<br>SET MEALS AT $0.99</h1>
    </div>

    <a class="cta" href="#">ORDER NOW</a>
  </div>
</body>
</html>
```